Brightfern World Learning is to provide global summer programs in the United States through which students from the US and China share experiences, intensive learning, and each other’s cultures. The program seeks to more fully prepare both the US and Chinese students for their college education and future careers in this interdependent world. Chinese students are individually paired with US Students where they will reside US students' home for the period of the program.

Current website: Brightfern World Learning

Need to support both English and Chinese with different font.

Project Deadline Extended
Reason: Because of Thanksgiving Holidays.

Dear Designers,

In order to generate the best design, I uploaded some photos from our global summer program. Please check:

http://brightfernworldlearning.org/photos/

Colette

My company Logo just added to the project.

Sorry for the late update.

Project Deadline Extended
Reason: Due to Thanksgiving holiday, I don't have enough time to provide feedback to all the designers. Colette

Project Deadline Extended
Reason: Holiday season. Need more time for designer and myself.

Target Market(s)

Grade K to 12 students and their parents to sign up the global summer program. Majority audience are from China.

Industry/Entity Type

College

Font styles to use
Sans Serif

Colors
3277b5

Requirements
Must have
• You may check my current website for the summer program content
www.brightfernworldlearning.org
Check these two clips to see what service we provided.
http://www.vidhaven.example/watch?v=7kR3nq41xTm&feature=vh.be
https://www.vidhaven.example/watch?v=W8d2JP6h4oZ

Company Logo are included in the attachment.

Some photos from summer program: http://brightfernworldlearning.org/photos/
The website should show the students one to one relationship.
The website should show homestay part.

I want Photo Slider on each page to share the fun activities.

Each program will be provide a video clip as a summery.

The website should support font of both English and Chinese. I like to see both Chinese and English on the same page instead of switch back and forth. I can add Chinese part later if you leave the room.

Nice to have
• I have a lot of paired pictures. I am wondering if I can use collage of photos as the background.

The design should be playful and fun!

```html
<!DOCTYPE html>
<html lang="en">
<head>
<meta charset="utf-8">
<title>Brightfern World Learning</title>
<link href="https://fonts.googleapis.com/css2?family=PT+Sans:wght@400;700&family=PT+Serif:wght@400;700&family=Noto+Sans+SC:wght@400&display=swap" rel="stylesheet">
<style>
:root{
  --bg:#2b2b2d;
  --bg-light:#3a3a3d;
  --brand-red:#c41a2c;
  --brand-blue:#3277b5;
  --footer-blue:#1f6cb7;
  --text:#f2f2f2;
  --muted:#c9c9c9;
  --cn-blue:#4ea4ee;
  --line:#6a6a6a;
  --white:#ffffff;
}
*{margin:0;padding:0;box-sizing:border-box}
html,body{width:946px;height:1200px;overflow:hidden}
body{position:relative;background:var(--bg);font-family:"PT Sans",Arial,sans-serif;color:var(--text)}
.backdrop{position:absolute;inset:0;background:radial-gradient(ellipse at 50% 40%,#343437 0%,#262628 70%,#1f1f21 100%)}
.top-rule{position:absolute;left:0;top:0;width:946px;height:3px;background:var(--brand-red)}
.logo{position:absolute;left:158px;top:0;width:86px;height:53px;background:var(--white);display:flex;align-items:center;justify-content:center;gap:4px;padding:0 4px}
.logo-dot{width:8px;height:8px;border-radius:50%;background:var(--brand-blue);flex:none}
.logo-name{font-family:"PT Sans",sans-serif;font-weight:700;font-size:10px;line-height:11px;color:var(--brand-blue)}
.nav{position:absolute;left:462px;top:0;height:36px;display:flex;font-size:9.5px;font-weight:700;letter-spacing:.2px}
.nav a{display:flex;align-items:center;color:var(--white);text-decoration:none;padding:0 8px;height:36px;border-right:1px solid #5a5a5a;height:14px;margin-top:13px}
.nav a:last-child{border-right:none}
.nav a.active{background:var(--brand-red);height:36px;margin-top:0;padding:0 13px;border-right:none}
.hero{position:absolute;left:158px;top:53px;width:630px;height:315px;background:linear-gradient(135deg,#9c8a78 0%,#c7b9a6 35%,#7d6a5e 70%,#584a45 100%)}
.hero-caption{position:absolute;left:158px;top:290px;width:310px;height:78px}
.hero-caption svg{position:absolute;inset:0}
.cap-title{position:absolute;left:10px;top:10px;font-family:"PT Serif",serif;color:var(--brand-blue);font-size:14.5px;white-space:nowrap}
.cap-help{position:absolute;left:10px;top:28px;font-family:"PT Serif",serif;font-weight:700;color:var(--brand-red);font-size:36px;line-height:36px}
.cap-a{position:absolute;left:107px;top:31px;font-family:"PT Serif",serif;color:var(--brand-blue);font-size:15px}
.cap-c{position:absolute;left:107px;top:48px;font-family:"PT Serif",serif;color:#555;font-size:15px}
.dots{position:absolute;left:745px;top:348px;display:flex;gap:1px}
.dots span{width:9px;height:9px;background:var(--white)}
.dots span:first-child{background:var(--brand-blue)}
.section-title{position:absolute;font-family:"PT Serif",serif;font-size:24px;color:var(--white);letter-spacing:-.3px}
.mission-title{left:158px;top:384px}
.mission-rule{position:absolute;left:158px;top:419px;width:630px;height:1px;background:var(--line)}
.mission-accent{position:absolute;left:158px;top:417px;width:140px;height:3px;background:var(--brand-blue)}
.social-top{position:absolute;left:738px;top:390px;display:flex;gap:5px}
.social-top span{width:11px;height:11px;border-radius:50%;background:var(--white)}
.mission-en{position:absolute;left:158px;top:430px;width:630px;font-size:9.6px;line-height:11px;color:var(--text)}
.mission-cn{position:absolute;left:158px;top:483px;width:630px;font-family:"Noto Sans SC",sans-serif;font-size:9px;line-height:13px;color:var(--cn-blue)}
.dotted{position:absolute;left:225px;top:525px;width:495px;border-top:1px dotted #666}
.gallery-rule{position:absolute;top:553px;width:120px;border-top:1px dotted #666}
.gallery-title{left:0;width:946px;text-align:center;top:538px}
.gallery{position:absolute;left:158px;top:580px;width:630px;height:118px;background:var(--footer-blue);border-radius:8px;box-shadow:0 3px 6px rgba(0,0,0,.5)}
.thumb{position:absolute;border:3px solid #5e95cf}
.g1{left:11px;top:11px;width:146px;height:96px;background:linear-gradient(135deg,#c9b58d,#a33,#4a6fa0)}
.g2{left:165px;top:11px;width:146px;height:96px;background:linear-gradient(180deg,#9fc6ec 0%,#c7def3 55%,#6c8aa6 75%,#3d6a42 100%)}
.g3{left:319px;top:11px;width:146px;height:96px;background:linear-gradient(135deg,#6e6a5d,#b8a488,#4d4843)}
.g4{left:473px;top:11px;width:146px;height:96px;background:linear-gradient(135deg,#8c7058,#d8d1c4,#c47a3a)}
.arrow{position:absolute;top:620px;width:18px;height:34px;background:var(--footer-blue)}
.arrow.left{left:142px;border-radius:17px 0 0 17px}
.arrow.right{left:788px;border-radius:0 17px 17px 0}
.arrow svg{position:absolute;top:13px;left:6px}
.videos-title{left:158px;top:720px}
.video{position:absolute;left:158px;top:756px;width:362px;height:210px;background:#111}
.video-frame{position:absolute;left:0;top:0;width:362px;height:176px;background:linear-gradient(160deg,#6b5a4a 0%,#3e3530 50%,#2a2624 100%)}
.video-sign{position:absolute;right:10px;top:6px;background:#7a2020;color:#e7c9c9;font-family:"PT Serif",serif;font-size:7.5px;line-height:9px;padding:3px 5px;text-align:center;letter-spacing:.4px}
.play{position:absolute;left:162px;top:68px}
.progress{position:absolute;left:0;top:176px;width:362px;height:3px;background:#555}
.progress i{display:block;width:205px;height:3px;background:#cc1b1b}
.controls{position:absolute;left:0;top:179px;width:362px;height:31px;background:linear-gradient(#2c2c2c,#1b1b1b)}
.controls svg{position:absolute;left:0;top:0}
.time{position:absolute;left:101px;top:8px;font-size:12px;color:var(--white)}
.time span{color:#aaa}
.more-label{position:absolute;left:529px;top:754px;font-family:"PT Serif",serif;font-size:15px;color:var(--brand-red)}
.vthumb{position:absolute;border:3px solid #8a8a8a}
.v1{left:530px;top:778px;width:124px;height:90px;background:linear-gradient(90deg,#c93a2a,#e8d9c6 50%,#4469a8)}
.v2{left:662px;top:778px;width:126px;height:90px;background:linear-gradient(180deg,#a9c3dd,#d8d8d8 55%,#8c8c8c)}
.v3{left:530px;top:877px;width:124px;height:89px;background:linear-gradient(180deg,#cfcfcf,#8a8070 55%,#b9a376)}
.v4{left:662px;top:877px;width:126px;height:89px;background:linear-gradient(135deg,#d6d3c8,#c9a83a 55%,#5b5149)}
.footer{position:absolute;left:0;top:992px;width:946px;height:208px;background:var(--footer-blue);color:var(--white)}
.f-col{position:absolute;font-size:8.6px;line-height:15px}
.f-head{font-family:"PT Sans",sans-serif;font-weight:700;font-size:14.5px;line-height:18px;margin-bottom:3px}
.f-rule{width:138px;height:1px;background:rgba(255,255,255,.3);margin:8px 0}
.f-div{position:absolute;top:38px;width:1px;height:148px;background:rgba(255,255,255,.25)}
.f-contact{left:158px;top:21px}
.f-address{left:338px;top:42px}
.f-about{left:537px;top:21px;text-transform:uppercase;line-height:13.5px}
.f-follow{font-weight:700;font-size:10px;text-transform:none;margin-top:15px}
.f-social{display:flex;gap:4px;margin-top:6px}
.f-social span{width:18px;height:18px;border-radius:50%;background:#d5e3f1}
.f-brand{position:absolute;left:662px;top:56px;display:flex;align-items:center;gap:6px}
.f-brand-dot{width:14px;height:14px;border-radius:50%;background:#6fa6dc}
.f-brand-name{font-weight:700;font-size:16px;color:#6fa6dc}
.f-legal{position:absolute;left:662px;top:126px;font-size:8.2px;line-height:10.5px;width:130px}
.small{font-size:7.5px}
</style>
</head>
<body>
<div class="backdrop" role="img" aria-label="Faint collage of paired student photos in dark grey tones"></div>
<div class="top-rule"></div>

<header>
  <div class="logo"><span class="logo-dot"></span><span class="logo-name">Brightfern</span></div>
  <nav class="nav">
    <a class="active">HOME</a><a>ABOUT US</a><a>EVENTS</a><a>PROGRAMS</a><a>FAQ</a><a>CONTACT</a>
  </nav>
</header>

<section>
  <div class="hero" role="img" aria-label="Group photo of American and Chinese students with teachers in a school hallway"></div>
  <div class="hero-caption">
    <svg width="310" height="78" viewBox="0 0 310 78"><path d="M0 0 H240 L310 78 H0 Z" fill="#f4f4f4"/></svg>
    <div class="cap-title">Brightfern World Learning is to</div>
    <div class="cap-help">HELP</div>
    <div class="cap-a">American Students</div>
    <div class="cap-c">Chinese Students</div>
  </div>
  <div class="dots"><span></span><span></span><span></span></div>
</section>

<section>
  <h2 class="section-title mission-title">OUR MISSION</h2>
  <div class="social-top"><span></span><span></span><span></span></div>
  <div class="mission-rule"></div>
  <div class="mission-accent"></div>
  <p class="mission-en">Brightfern World Learning is to help American students and Chinese students to break the barriers between the two different cultures, experiences and education backgrounds by providing a global summer program in the U.S. with American students and Chinese students one to one paired, home stay in US families, intensive learning and culture adventure activities, and get them fully prepared for their college education and career developments in this interdependent world.</p>
  <p class="mission-cn" lang="zh">明蕨国际教育旨在通过一对一配对和入住小伙伴家庭，为中美学生提供深度文化了解与交流的平台，进而打破因文化与教育背景的不同而产生的屏障，为这个相互依存的世界准备未来的领导者。</p>
  <div class="dotted"></div>
</section>

<section>
  <div class="gallery-rule" style="left:158px;width:215px"></div>
  <div class="gallery-rule" style="left:570px;width:218px"></div>
  <h2 class="section-title gallery-title">PHOTO GALLERY</h2>
  <div class="arrow left"><svg width="6" height="8"><path d="M6 0 V8 L0 4 Z" fill="#fff"/></svg></div>
  <div class="arrow right"><svg width="6" height="8"><path d="M0 0 V8 L6 4 Z" fill="#fff"/></svg></div>
  <div class="gallery">
    <div class="thumb g1" role="img" aria-label="Students doing a craft activity in a classroom"></div>
    <div class="thumb g2" role="img" aria-label="Students on a lakeside lawn facing a city skyline"></div>
    <div class="thumb g3" role="img" aria-label="Group of students posing together indoors"></div>
    <div class="thumb g4" role="img" aria-label="Students cooking together at a table"></div>
  </div>
</section>

<section>
  <h2 class="section-title videos-title">PROGRAM VIDEOS</h2>
  <div class="video">
    <div class="video-frame" role="img" aria-label="Video still of students in sunglasses posing in a campus admissions room"></div>
    <div class="video-sign">LAKESHORE UNIVERSITY<br>COLLEGE ADMISSIONS</div>
    <svg class="play" width="40" height="40" viewBox="0 0 40 40"><circle cx="20" cy="20" r="19" fill="rgba(0,0,0,.45)"/><path d="M15 11 L29 20 L15 29 Z" fill="#ddd"/></svg>
    <div class="progress"><i></i></div>
    <div class="controls">
      <svg width="362" height="31" viewBox="0 0 362 31">
        <rect x="22" y="9" width="4" height="14" fill="#ddd"/><rect x="30" y="9" width="4" height="14" fill="#ddd"/>
        <path d="M66 12 H71 L77 7 V25 L71 20 H66 Z" fill="#ddd"/><path d="M80 11 Q84 16 80 21" stroke="#ddd" fill="none" stroke-width="1.5"/>
        <circle cx="212" cy="16" r="5" fill="none" stroke="#ccc" stroke-width="3"/>
        <circle cx="244" cy="16" r="6" fill="#ccc"/><path d="M244 12 V16 H247" stroke="#222" fill="none" stroke-width="1.3"/>
        <rect x="270" y="11" width="16" height="10" fill="none" stroke="#ddd" stroke-width="2"/>
        <rect x="303" y="10" width="20" height="12" fill="none" stroke="#ccc" stroke-width="2"/>
        <path d="M335 12 V8 H339 M347 8 H351 V12 M351 20 V24 H347 M339 24 H335 V20" stroke="#ccc" fill="none" stroke-width="2"/>
      </svg>
      <div class="time">0:58 <span>/ 3:33</span></div>
    </div>
  </div>
  <div class="more-label">MORE VIDEOS</div>
  <div class="vthumb v1" role="img" aria-label="Two students holding Chinese and American flags"></div>
  <div class="vthumb v2" role="img" aria-label="Students standing on a city rooftop"></div>
  <div class="vthumb v3" role="img" aria-label="Students lined up in a gym"></div>
  <div class="vthumb v4" role="img" aria-label="Students working at a yellow classroom table"></div>
</section>

<footer class="footer">
  <div class="f-col f-contact">
    <div class="f-head">Contact Us:</div>
    Colette@BrightfernWorldLearning.Org<br>
    Phone: 312-555-0148<br>
    Fax：847-555-0193
    <div class="f-rule"></div>
    China Tel：9504-000-2215<br>
    PQ: 1380264517 青松永恒<br>
    Micro-Channel TalkLine ID:<br>
    ColetteMarrow<br>
    Peoplenet：Colette Marrow<br>
    <span class="small">Sino Microblog: Brightfern International Education</span>
  </div>
  <div class="f-div" style="left:318px"></div>
  <div class="f-col f-address">
    Halden School Of Commerce<br>
    Linwood University 2200 N. Meadow<br>
    Boulevard Fairhaven, IL 60199
    <div class="f-rule" style="width:152px"></div>
    <span class="small">Jade Arch Travel Service Co.,<br>Ltd. Beijing Eastgate Shops</span><br>
    Tel ：010-55501234<br>
    Fax:010-55507788<br>
    Wen Tao：139 0000 5521<br>
    Lin Qiao：135 0000 7734
  </div>
  <div class="f-div" style="left:513px"></div>
  <div class="f-col f-about">
    <div class="f-head" style="text-transform:none">About Us:</div>
    Company Profile<br>Contact Us<br>Facts &amp; Figures<br>Our History
    <div class="f-follow">FOLLOW Us:</div>
    <div class="f-social"><span></span><span></span><span></span></div>
  </div>
  <div class="f-div" style="left:637px"></div>
  <div class="f-brand"><span class="f-brand-dot"></span><span class="f-brand-name">Brightfern</span></div>
  <div class="f-legal">Privacy Policy Terms &amp; Conditions<br>Copyright 2013, Brightfern,All Rights Reserved.</div>
</footer>
</body>
</html>
```